Looking for an amazing business card for a thriving DJ business

We need a business card design for a DJ company based in South Florida. The DJ company specializes in weddings, parties, bar mitzvahs, corporate events, proms, and reunions. We are looking for a modern, simple business card design. The card should state DJ Marlow K.
Updates

The name on the card should be DJ Marlow K

Industry/Entity Type

Entertainment Industry

Contact Information for Business Card

DJ Marlow K
512.447.2086
atxdjmarlowk@quellmail.com
https://www.facebook.com/DjMarlowK/
https://www.instagram.com/djmarlow.k/
www.djmarlowk.net

Font styles to use
Serif
Sans Serif

Requirements
Must have
• My business card has to be awesome.
Should not have
• The card has to have personality.

```html
<!DOCTYPE html>
<html lang="en">
<head>
<meta charset="utf-8">
<title>DJ Marlow K — Business Card</title>
<link rel="stylesheet" href="https://fonts.googleapis.com/css2?family=Delius&family=Roboto:wght@300;400&display=swap">
<style>
  :root {
    --page: #e9e8e6;
    --card: #ffffff;
    --card-shade: #f3f3f2;
    --gold: #b08f3e;
    --gold-soft: #efe6cf;
    --ink: #5b5b5b;
    --rule: #8a8a8a;
    --ghost: #ececec;
  }
  * { margin: 0; padding: 0; box-sizing: border-box; }
  html, body {
    width: 1200px; height: 985px; overflow: hidden;
    background: var(--page);
  }
  .sheet {
    position: relative; width: 1200px; height: 985px;
    display: flex; flex-direction: column; align-items: center;
    justify-content: center; gap: 40px;
  }
  .card {
    position: relative; width: 760px; height: 434px;
    background: linear-gradient(160deg, var(--card) 40%, var(--card-shade) 100%);
    border-right: 4px solid var(--gold);
    border-bottom: 4px solid var(--gold);
    box-shadow: 0 10px 24px rgba(0,0,0,0.18);
    overflow: hidden;
  }
  .brand-badge {
    position: absolute; width: 190px; height: 190px;
    border: 2px solid var(--gold); border-radius: 50%;
    display: flex; align-items: center; justify-content: center;
    text-align: center;
    font-family: "Delius", sans-serif; color: var(--ink);
    font-size: 22px; line-height: 1.25; padding: 24px;
  }
  .card--front .brand-badge { left: 285px; top: 122px; }
  .card--back .brand-badge { left: 36px; top: 26px; width: 160px; height: 160px; font-size: 19px; }
  .brand-ghost {
    position: absolute; left: 300px; top: 170px; width: 430px;
    font-family: "Delius", sans-serif; font-size: 74px; line-height: 1;
    color: var(--ghost); text-align: center;
  }
  .holder-name {
    position: absolute; left: 40px; top: 206px;
    font-family: "Delius", sans-serif; font-size: 34px;
    color: var(--gold); letter-spacing: 1px;
  }
  .name-rule {
    position: absolute; left: 40px; top: 254px; width: 680px;
    height: 1.5px; background: var(--rule);
  }
  .contact-list {
    position: absolute; left: 40px; top: 268px; list-style: none;
    font-family: "Roboto", sans-serif; font-weight: 300;
    font-size: 21px; color: var(--ink);
  }
  .contact-list li { display: flex; align-items: center; gap: 14px; height: 32px; }
  .contact-list svg { width: 18px; height: 18px; flex: none; }
  .accent { color: var(--gold); }
  .social-list {
    position: absolute; right: 44px; bottom: 30px; list-style: none;
    font-family: "Roboto", sans-serif; font-weight: 300;
    font-size: 21px; color: var(--ink);
  }
  .social-list li { display: flex; align-items: center; gap: 10px; height: 32px; }
  .social-mark {
    width: 16px; height: 16px; border: 2px solid var(--gold); border-radius: 3px; flex: none;
  }
</style>
</head>
<body>
<main class="sheet">
  <section class="card card--front">
    <div class="brand-badge">Velvet Booth Events</div>
  </section>

  <section class="card card--back">
    <div class="brand-ghost">Velvet Booth Events</div>
    <div class="brand-badge">Velvet Booth Events</div>
    <h1 class="holder-name">DJ Marlow K</h1>
    <div class="name-rule"></div>
    <ul class="contact-list">
      <li>
        <svg viewBox="0 0 24 24" fill="none" stroke="var(--gold)" stroke-width="2.4" stroke-linecap="round"><path d="M6 3c-2 2-2 6 2 11s9 7 11 5l-3-4-3 1c-2-1-4-4-5-6l1-3z"/></svg>
        512.447.2086
      </li>
      <li>
        <svg viewBox="0 0 24 24" fill="none" stroke="var(--gold)" stroke-width="2"><rect x="3" y="6" width="18" height="12" rx="1"/><path d="M3 6l9 7 9-7"/></svg>
        atxdjmarlowk@quellmail.com
      </li>
      <li>
        <svg viewBox="0 0 24 24" fill="none" stroke="var(--gold)" stroke-width="2"><circle cx="12" cy="12" r="9"/><path d="M3 12h18M12 3c3 3 3 15 0 18M12 3c-3 3-3 15 0 18"/></svg>
        <span>www.<span class="accent">djmarlowk</span>.net</span>
      </li>
    </ul>
    <ul class="social-list">
      <li><span class="social-mark"></span>DjMarlowK/</li>
      <li><span class="social-mark"></span>djmarlow.k/</li>
    </ul>
  </section>
</main>
</body>
</html>
```